Store Promo Card (already have logo!)

I need a card design (single side) for my online women’s gift shop containing a promotional code to be placed in bags for attendees at an event. I’m flexible on both shape and sizing, but perhaps a 4x6 card.
—It should contain my attached logo, my website (www.merrowlyn.com), and my Instagram handle (@merrowlyn) and promotion language such as “15% off your purchase with code: PIVRAL”.
—I think I would like my logo to be large.
—It should be clean, simple and modern in design and should use the colors from my logo.
—I would like about 3-5 product pictures depending on design.
Target Market(s)
Women ages 30 to 60
Industry/Entity Type
Retail Upscale Gift

```html
<!DOCTYPE html>
<html lang="en">
<head>
<meta charset="utf-8">
<title>Merrowlyn Promo Card</title>
<link rel="stylesheet" href="https://fonts.googleapis.com/css2?family=Cinzel:wght@600;700&family=Montserrat:wght@600&display=swap">
<style>
  :root {
    --backdrop: #e6e4e6;
    --blush: #efd2ce;
    --slate: #606062;
    --ink: #111111;
    --paper: #ffffff;
  }
  html, body {
    margin: 0;
    padding: 0;
    overflow: hidden;
  }
  body {
    width: 1200px;
    height: 1025px;
    background: var(--backdrop);
    position: relative;
  }
  .promo-card {
    position: absolute;
    left: 120px;
    top: 32px;
    width: 960px;
    height: 960px;
    background: var(--blush);
    overflow: hidden;
  }
  .brand-name {
    position: absolute;
    top: 190px;
    left: 0;
    width: 100%;
    margin: 0;
    text-align: center;
    font-family: "Cinzel", serif;
    font-weight: 700;
    font-size: 92px;
    line-height: 1;
    letter-spacing: 2px;
    color: var(--slate);
  }
  .offer {
    position: absolute;
    top: 442px;
    left: 0;
    width: 100%;
    margin: 0;
    text-align: center;
    font-family: "Cinzel", serif;
    font-weight: 700;
    font-size: 45px;
    line-height: 1;
    color: var(--ink);
  }
  .code-box {
    position: absolute;
    left: 263px;
    top: 537px;
    width: 466px;
    height: 129px;
    background: var(--paper);
  }
  .code-box .code-frame {
    position: absolute;
    inset: 14px;
    border: 2px dashed var(--slate);
    display: flex;
    align-items: center;
    justify-content: center;
  }
  .code-box .code {
    font-family: "Cinzel", serif;
    font-weight: 700;
    font-size: 58px;
    letter-spacing: 6px;
    color: var(--slate);
    line-height: 1;
  }
  .contact-band {
    position: absolute;
    left: 0;
    bottom: 0;
    width: 100%;
    height: 147px;
    background: var(--slate);
  }
  .contact-item {
    position: absolute;
    top: 40px;
    display: flex;
    align-items: center;
    gap: 12px;
    font-family: "Montserrat", sans-serif;
    font-weight: 600;
    font-size: 33px;
    color: var(--paper);
  }
  .contact-item.social { left: 41px; }
  .contact-item.web { left: 440px; }
  .contact-icon {
    width: 65px;
    height: 65px;
    flex: none;
  }
</style>
</head>
<body>
  <main class="promo-card">
    <h1 class="brand-name">MERROWLYN</h1>
    <p class="offer">15% OFF YOUR PURCHASE</p>
    <div class="code-box">
      <div class="code-frame"><span class="code">PIVRAL</span></div>
    </div>
    <footer class="contact-band">
      <div class="contact-item social">
        <svg class="contact-icon" viewBox="0 0 65 65" aria-hidden="true">
          <circle cx="32.5" cy="32.5" r="32.5" fill="#ffffff"/>
        </svg>
        <span>@merrowlyn</span>
      </div>
      <div class="contact-item web">
        <svg class="contact-icon" viewBox="0 0 65 65" aria-hidden="true">
          <circle cx="32.5" cy="32.5" r="32.5" fill="#ffffff"/>
          <g fill="none" stroke="#606062" stroke-width="2.5">
            <circle cx="32.5" cy="32.5" r="18"/>
            <ellipse cx="32.5" cy="32.5" rx="8" ry="18"/>
            <line x1="14.5" y1="32.5" x2="50.5" y2="32.5"/>
            <line x1="17" y1="23" x2="48" y2="23"/>
            <line x1="17" y1="42" x2="48" y2="42"/>
          </g>
        </svg>
        <span>www.merrowlyn.com</span>
      </div>
    </footer>
  </main>
</body>
</html>
```